Professional business cards for real estate development company

I need business cards for my new real estate development company. The company, "LUMAR" is a real estate development, investment, and advisory firm with a focus on multifamily, office, and mixed-use projects across primary and secondary markets in the Southeast United States.

Style preference is modern

Industry/Entity Type

Real Estate Development

Contact Information for Business Card

The business cards need to include:
Name
Title
Mailing Address
Phone Number
Web Address

Logo is attached. I would like white to be the primary color with incorporation of the company colors: #232D3A and #B5A451

Font styles to use
Other font styles liked:
• Montserrat, Avenir

Requirements
Must have
• Company Logo. No need to include the company name since the name is in the logo.
Should not have
• No line type designs

```html
<!DOCTYPE html>
<html lang="en">
<head>
<meta charset="UTF-8">
<title>LUMAR Development – Business Card</title>
<link rel="stylesheet" href="https://fonts.googleapis.com/css2?family=Montserrat:wght@400;500;600&display=swap">
<style>
  :root {
    --navy: #232D3A;
    --gold: #B5A451;
    --white: #FFFFFF;
    --paper: #F7F7F5;
    --backdrop: #121821;
  }
  * { box-sizing: border-box; margin: 0; padding: 0; }
  html, body {
    width: 1200px; height: 876px; overflow: hidden;
    background: var(--backdrop);
    font-family: "Montserrat", sans-serif;
  }
  .canvas {
    width: 1200px; height: 876px;
    display: flex; flex-direction: column;
    align-items: center; justify-content: center; gap: 40px;
  }
  .card {
    width: 560px; height: 320px;
    border-radius: 14px;
    position: relative;
    overflow: hidden;
  }
  /* Front */
  .card-front { background: var(--paper); color: var(--navy); }
  .brand {
    position: absolute; left: 40px; top: 0; bottom: 0; width: 190px;
    display: flex; align-items: center; gap: 10px;
  }
  .brand-square { width: 14px; height: 14px; background: var(--navy); flex: none; }
  .brand-name {
    font-weight: 600; font-size: 36px; letter-spacing: 3px; color: var(--navy);
  }
  .divider-vertical {
    position: absolute; left: 250px; top: 52px; width: 1.5px; height: 216px;
    background: var(--gold);
  }
  .details { position: absolute; left: 276px; top: 58px; width: 250px; }
  .person-name { font-weight: 500; font-size: 28px; color: var(--gold); line-height: 1.1; }
  .person-title { font-size: 10.5px; margin-top: 6px; color: var(--navy); }
  .divider-horizontal { height: 1.5px; background: var(--gold); margin: 12px 0 18px; }
  .contact-list { list-style: none; }
  .contact-item {
    display: flex; align-items: center; gap: 8px;
    font-size: 15px; font-weight: 500; color: var(--navy);
    margin-bottom: 9px; white-space: nowrap;
  }
  .contact-icon { width: 13px; height: 13px; flex: none; }
  /* Back */
  .card-back {
    background: var(--navy);
    display: flex; align-items: center; justify-content: center; gap: 14px;
  }
  .card-back .brand-square { background: var(--gold); width: 16px; height: 16px; }
  .card-back .brand-name { color: var(--white); font-size: 44px; letter-spacing: 5px; }
</style>
</head>
<body>
<main class="canvas">
  <section class="card card-front" aria-label="Business card front">
    <div class="brand">
      <span class="brand-square"></span>
      <span class="brand-name">LUMAR</span>
    </div>
    <div class="divider-vertical"></div>
    <div class="details">
      <h1 class="person-name">Daniel K. Marsh</h1>
      <p class="person-title">Managing Director Of LUMAR Development</p>
      <div class="divider-horizontal"></div>
      <ul class="contact-list">
        <li class="contact-item">
          <svg class="contact-icon" viewBox="0 0 24 24" aria-hidden="true"><path fill="#B5A451" d="M6.6 10.8a15.1 15.1 0 0 0 6.6 6.6l2.2-2.2c.3-.3.7-.4 1-.2 1.1.4 2.3.6 3.6.6.6 0 1 .4 1 1V20c0 .6-.4 1-1 1A17 17 0 0 1 3 4c0-.6.4-1 1-1h3.5c.6 0 1 .4 1 1 0 1.3.2 2.5.6 3.6.1.3 0 .7-.2 1z"/></svg>
          <span>555 014 2208</span>
        </li>
        <li class="contact-item">
          <svg class="contact-icon" viewBox="0 0 24 24" aria-hidden="true"><rect x="2" y="5" width="20" height="14" rx="1.5" fill="#B5A451"/><path d="M3 6l9 7 9-7" stroke="#F7F7F5" stroke-width="1.6" fill="none"/></svg>
          <span>info@lumardevelopment.com</span>
        </li>
        <li class="contact-item">
          <svg class="contact-icon" viewBox="0 0 24 24" aria-hidden="true"><circle cx="12" cy="12" r="10" fill="#B5A451"/><path d="M2 12h20M12 2c3 3 3 17 0 20M12 2c-3 3-3 17 0 20" stroke="#F7F7F5" stroke-width="1.3" fill="none"/></svg>
          <span>www.lumardevelopment.com</span>
        </li>
      </ul>
    </div>
  </section>
  <section class="card card-back" aria-label="Business card back">
    <span class="brand-square"></span>
    <span class="brand-name">LUMAR</span>
  </section>
</main>
</body>
</html>
```